Biz Card for Harrowfield Property Partners - HWPP

Harrowfield Property Partners is a commercial real estate acquisitions firm. We buy commercial property and need to raise capital from investors for each deal we buy. The vibe needs to be: give us your money, we will multiply it.
Our website: www.hrwpp-example.com
Competitors are: https://velmarholdings-example.com/, https://tribanquepartners-example.com/, http://www.ostrellecapital-example.com/
Target Market(s)
High Net Worth Individuals, Bankers, Insurance Companies, Commercial Real Estate Brokers.
Industry/Entity Type
Investment Banking
Contact Information for Business Card
Name, Title, Addess, Cell#, Office#, email, website
Requirements
Must have
- use one of our logos. See website for look and feel: www.hrwpp-example.com
Nice to have
- see website: www.hrwpp-example.com

```html
<!DOCTYPE html>
<html lang="en">
<head>
<meta charset="utf-8">
<title>Harrowfield Property Partners — Stationery</title>
<link rel="stylesheet" href="https://fonts.googleapis.com/css2?family=Nunito+Sans:wght@300;400;700&family=Arimo:wght@400;700&family=Cedarville+Cursive&display=swap">
<style>
  :root {
    --navy: #03243b;
    --paper: #f5f5f5;
    --stage: #e3e3e3;
    --band-grey: #b3aeac;
    --ink: #1b1b1b;
    --muted: #5a5f66;
    --mark-faint: #e6e6e6;
    --rule: #3f5d78;
  }
  * { box-sizing: border-box; margin: 0; padding: 0; }
  html, body { width: 1200px; height: 1200px; overflow: hidden; }
  body { background: var(--stage); position: relative; font-family: "Nunito Sans", sans-serif; }

  /* ---------- Letterhead ---------- */
  .letterhead {
    position: absolute; left: 109px; top: 184px; width: 658px; height: 851px;
    background: var(--paper); overflow: hidden;
  }
  .brand { position: absolute; display: flex; align-items: center; color: var(--navy); font-weight: 400; }
  .brand-dot { border-radius: 50%; background: var(--navy); flex: none; }
  .brand-name { line-height: 1; text-transform: uppercase; }
  .brand-name .line { display: block; }

  .letterhead .brand { left: 53px; top: 43px; }
  .letterhead .brand-dot { width: 65px; height: 65px; margin-right: 14px; }
  .letterhead .brand-name .line-main { font-size: 25px; letter-spacing: 5px; }
  .letterhead .brand-name .line-sub { font-size: 10px; letter-spacing: 4.6px; margin-top: 7px; }

  .contact-block {
    position: absolute; left: 466px; top: 48px; padding-left: 9px;
    border-left: 1px solid var(--rule);
    font-size: 10px; line-height: 13px; color: var(--ink); font-weight: 400;
  }
  .contact-block .row { display: flex; align-items: center; gap: 4px; }
  .contact-block .gap { margin-top: 3px; }
  .icon { width: 9px; height: 9px; fill: var(--navy); flex: none; }

  .watermark {
    position: absolute; left: 165px; top: 262px; width: 326px; height: 326px;
    border-radius: 50%; background: var(--mark-faint);
  }
  .letter-body {
    position: absolute; left: 53px; top: 227px; width: 550px;
    font-family: "Arimo", sans-serif; font-size: 9.4px; line-height: 13px; color: var(--ink);
  }
  .letter-body p { text-align: justify; margin-bottom: 13px; }
  .letter-body .date { margin-bottom: 30px; }
  .letter-body .salutation { font-weight: 700; margin-bottom: 26px; }
  .letter-body .closing { margin-top: 33px; margin-bottom: 10px; text-align: left; }
  .signature { font-family: "Cedarville Cursive", cursive; font-size: 17px; line-height: 20px; color: #222; margin-bottom: 10px; }
  .signer { line-height: 13px; }

  .footer-band { position: absolute; left: 0; bottom: 0; width: 658px; height: 27px; }
  .footer-url {
    position: absolute; right: 43px; bottom: 7px; color: #fff; font-size: 10px; letter-spacing: 0.2px;
  }
  .footer-url b { font-weight: 700; }

  /* ---------- Cards ---------- */
  .card { position: absolute; left: 820px; width: 271px; height: 155px; overflow: hidden; }
  .card-front { top: 320px; background: var(--navy); color: #fff; text-align: center; }
  .card-front .front-dot {
    position: absolute; left: 113px; top: 37px; width: 44px; height: 44px; border-radius: 50%; background: var(--paper);
  }
  .card-front .front-name {
    position: absolute; left: 0; right: 0; top: 84px; text-transform: uppercase; font-weight: 400; line-height: 1;
  }
  .card-front .front-name .line-main { display: block; font-size: 17px; letter-spacing: 3.4px; }
  .card-front .front-name .line-sub { display: block; font-size: 6px; letter-spacing: 2.6px; margin-top: 4px; }
  .card-front .front-url {
    position: absolute; left: 0; right: 0; top: 131px; font-size: 6.5px; letter-spacing: 2px;
  }
  .card-front .front-url b { font-weight: 700; }

  .card-back { top: 520px; background: var(--paper); }
  .card-back .brand { left: 18px; top: 15px; }
  .card-back .brand-dot { width: 30px; height: 30px; margin-right: 6px; }
  .card-back .brand-name .line-main { font-size: 11px; letter-spacing: 2px; }
  .card-back .brand-name .line-sub { font-size: 4px; letter-spacing: 1.6px; margin-top: 3px; }

  .holder { position: absolute; right: 19px; top: 61px; text-align: right; color: var(--navy); }
  .holder-name { font-size: 9px; font-weight: 700; line-height: 11px; }
  .holder-title { font-size: 6px; color: var(--muted); line-height: 8px; }
  .holder-rule { position: absolute; left: 18px; right: 19px; top: 86px; border-top: 1px solid var(--rule); }

  .card-contact { position: absolute; left: 18px; top: 91px; font-size: 6px; line-height: 9px; color: var(--muted); }
  .card-contact .row { display: flex; align-items: center; gap: 3px; }
  .card-contact .gap { margin-top: 2px; }
  .card-contact .icon { width: 6px; height: 6px; }

  .card-band { position: absolute; left: 0; bottom: 0; width: 271px; height: 15px; }
  .card-url { position: absolute; right: 19px; bottom: 4px; color: #fff; font-size: 6px; }
  .card-url b { font-weight: 700; }
</style>
</head>
<body>

<section class="letterhead" aria-label="Letterhead">
  <div class="brand">
    <span class="brand-dot"></span>
    <span class="brand-name">
      <span class="line line-main">Harrowfield</span>
      <span class="line line-sub">Property Partners</span>
    </span>
  </div>

  <address class="contact-block" style="font-style:normal">
    <div>48 Larkspur Way, Suite 610</div>
    <div>Fenmore, FL 33990</div>
    <div class="row gap">
      <svg class="icon" viewBox="0 0 24 24"><path d="M6.6 10.8a15.1 15.1 0 0 0 6.6 6.6l2.2-2.2a1 1 0 0 1 1-.25 11.4 11.4 0 0 0 3.6.57 1 1 0 0 1 1 1V20a1 1 0 0 1-1 1A17 17 0 0 1 3 4a1 1 0 0 1 1-1h3.5a1 1 0 0 1 1 1c0 1.25.2 2.45.57 3.57a1 1 0 0 1-.25 1z"/></svg>
      (555) 014-2290
    </div>
    <div class="row">
      <svg class="icon" viewBox="0 0 24 24"><path d="M2 5h20v14H2zM4 7v.5l8 5.5 8-5.5V7zm0 2.9V17h16V9.9l-8 5.5z"/></svg>
      dmarrow@hrwpp-example.com
    </div>
  </address>

  <div class="watermark" aria-hidden="true"></div>

  <div class="letter-body">
    <p class="date">July 30, 2020</p>
    <p class="salutation">Dear Mr. Avery,</p>
    <p>Lorem ipsum dolor sit amet, consectetur adipiscing elit. Integer diam quam, egestas eu ultrices eu, suscipit ac sapien. Phasellus eu dui nisi. Nam et euismod diam, nec lobortis tortor. Donec et diam nulla. Aenean varius tincidunt convallis. Aliquam a tortor at lacus dictum aliquet. Nunc laoreet metus sapien, in scelerisque augue consectetur in.</p>
    <p>Fusce nec justo laoreet, egestas justo sed, aliquet sem. Pellentesque pharetra massa non orci bibendum semper. Pellentesque cursus eu lectus a consectetur. Nunc volutpat suscipit posuere. Vestibulum facilisis vel quam malesuada mattis. Nulla in mattis tellus. Maecenas tristique mauris vitae pharetra tincidunt. In ut ornare risus. Integer molestie vestibulum nisi, semper dapibus mi condimentum eu.</p>
    <p>Nullam sagittis elit libero, id fringilla est tincidunt eget. Donec in ipsum ultricies, consectetur quam vel, facilisis elit. Phasellus tincidunt congue risus vel luctus. Suspendisse ut mollis neque. Donec ornare orci in turpis vestibulum, in ultrices metus scelerisque. Pellentesque mattis mattis nunc, nec tincidunt lacus egestas id. Fusce facilisis sagittis neque sit amet vulputate. Aliquam ut eros lobortis tortor facilisis vehicula. Sed sed luctus leo, at laoreet sapien. Donec placerat adipiscing ligula non euismod. In lobortis pretium nisl id luctus.</p>
    <p>Integer gravida tincidunt nibh, scelerisque tincidunt turpis. Suspendisse potenti. Nunc hendrerit euismod lectus id elementum. Fusce vitae gravida velit, quis eleifend lectus. In imperdiet mauris eu dui viverra sagittis. Donec tempor dui diam, condimentum gravida lacus pretium a. Nullam fringilla augue quis arcu placerat scelerisque. Aliquam nec tincidunt augue, sit amet posuere ipsum.</p>
    <p class="closing">Sincerely Yours,</p>
    <div class="signature">Daniel Marrow</div>
    <div class="signer">Daniel Marrow<br>Managing Partner Multifamily</div>
  </div>

  <svg class="footer-band" viewBox="0 0 658 27" aria-hidden="true">
    <polygon points="0,10 479,10 471,27 0,27" fill="var(--band-grey)"/>
    <polygon points="487,0 658,0 658,27 474,27" fill="var(--navy)"/>
  </svg>
  <div class="footer-url">www.<b>hrwpp-example</b>.com</div>
</section>

<section class="card card-front" aria-label="Business card front">
  <span class="front-dot"></span>
  <div class="front-name">
    <span class="line-main">Harrowfield</span>
    <span class="line-sub">Property Partners</span>
  </div>
  <div class="front-url">www.<b>hrwpp-example</b>.com</div>
</section>

<section class="card card-back" aria-label="Business card back">
  <div class="brand">
    <span class="brand-dot"></span>
    <span class="brand-name">
      <span class="line line-main">Harrowfield</span>
      <span class="line line-sub">Property Partners</span>
    </span>
  </div>

  <div class="holder">
    <div class="holder-name">Daniel Marrow</div>
    <div class="holder-title">Managing Partner Multifamily</div>
  </div>
  <div class="holder-rule"></div>

  <div class="card-contact">
    <div>48 Larkspur Way, Suite 610</div>
    <div>Fenmore, FL 33990</div>
    <div class="row gap">
      <svg class="icon" viewBox="0 0 24 24"><path d="M7 1h10a2 2 0 0 1 2 2v18a2 2 0 0 1-2 2H7a2 2 0 0 1-2-2V3a2 2 0 0 1 2-2zm0 3v14h10V4z"/></svg>
      (555) 014-2290
    </div>
    <div class="row">
      <svg class="icon" viewBox="0 0 24 24"><path d="M6.6 10.8a15.1 15.1 0 0 0 6.6 6.6l2.2-2.2a1 1 0 0 1 1-.25 11.4 11.4 0 0 0 3.6.57 1 1 0 0 1 1 1V20a1 1 0 0 1-1 1A17 17 0 0 1 3 4a1 1 0 0 1 1-1h3.5a1 1 0 0 1 1 1c0 1.25.2 2.45.57 3.57a1 1 0 0 1-.25 1z"/></svg>
      (555) 014-2291
    </div>
    <div class="row">
      <svg class="icon" viewBox="0 0 24 24"><path d="M2 5h20v14H2zM4 7v.5l8 5.5 8-5.5V7zm0 2.9V17h16V9.9l-8 5.5z"/></svg>
      dmarrow@hrwpp-example.com
    </div>
  </div>

  <svg class="card-band" viewBox="0 0 271 15" aria-hidden="true">
    <polygon points="0,7 170,7 166,15 0,15" fill="var(--band-grey)"/>
    <polygon points="175,0 271,0 271,15 168,15" fill="var(--navy)"/>
  </svg>
  <div class="card-url">www.<b>hrwpp-example</b>.com</div>
</section>

</body>
</html>
```